business card design.

2 sided transparent design like my current card with the attached logo. Super simple, should take someone 5-10 minutes tops. Cell number will be embossed. You could put the web URL on the back of the logo with white blocker background as www.vex-kl.com. The chip is foil to make it look like a credit card. Any suggested ways to improve the design are welcome. The mag stripe should be printed on the back of the card. Instead of Brimly the company name will be Vex

```html
<!DOCTYPE html>
<html lang="en">
<head>
<meta charset="utf-8">
<title>Dana Mercer – Business Card</title>
<link rel="stylesheet" href="https://fonts.googleapis.com/css2?family=Open+Sans:wght@300;400;700&display=swap">
<style>
  :root {
    --page-bg: #e3e5e8;
    --card-face: rgba(246, 246, 247, 0.94);
    --card-band: #d2d3d5;
    --mag-stripe: #383838;
    --ink: #111111;
    --ink-soft: #555555;
    --ink-muted: #6a6a6a;
    --blocker: #ffffff;
    --foil-light: #e8c65a;
    --foil-dark: #b58f25;
    --foil-line: #5a4410;
    --brand-dot: #f06a6a;
  }
  * { box-sizing: border-box; margin: 0; padding: 0; }
  html, body {
    width: 1057px; height: 1200px; overflow: hidden;
    background: var(--page-bg);
    font-family: "Open Sans", Arial, sans-serif;
  }
  .canvas { position: relative; width: 1057px; height: 1200px; }

  .card {
    position: absolute; width: 768px; height: 497px;
    background: var(--card-face);
    border-radius: 20px;
    box-shadow: 4px 6px 14px rgba(0,0,0,0.28);
    overflow: hidden;
  }
  .card--front { left: 148px; top: 73px; }
  .card--back  { left: 154px; top: 634px; }

  .band { position: absolute; left: 0; right: 0; top: 43px; height: 65px; }
  .band--clear { background: var(--card-band); }
  .band--magstripe { background: var(--mag-stripe); }

  .chip { position: absolute; width: 82px; height: 74px; }
  .card--front .chip { left: 111px; top: 140px; }
  .card--back .chip { left: 575px; top: 139px; }

  .holder-name {
    position: absolute; font-size: 54px; line-height: 1; color: var(--ink);
    letter-spacing: -1px; white-space: nowrap;
  }
  .holder-name .given { font-weight: 300; }
  .holder-name .family { font-weight: 700; }

  .contact-line { position: absolute; display: flex; align-items: center; white-space: nowrap; }
  .contact-line svg { flex: none; }
  .phone-number {
    font-size: 36px; font-weight: 700; color: var(--ink-muted);
    word-spacing: 18px; margin-left: 20px;
  }
  .email-address {
    font-size: 29px; font-weight: 400; color: var(--ink);
    margin-left: 20px;
  }

  .front-details .holder-name { left: 52px; top: 268px; }
  .front-details .contact-phone { left: 50px; top: 380px; }
  .front-details .contact-email { left: 50px; top: 430px; }

  .brand-lockup {
    position: absolute; left: 470px; top: 345px;
    display: flex; align-items: center; gap: 16px;
  }
  .brand-dot { width: 58px; height: 58px; border-radius: 50%; background: var(--brand-dot); }
  .brand-name { font-size: 60px; font-weight: 700; color: var(--ink); line-height: 1; }

  .mirrored {
    position: absolute; right: 52px; top: 0; width: 520px; height: 497px;
    transform: scaleX(-1);
  }
  .mirrored .holder-name { left: 0; top: 268px; }
  .mirrored .contact-phone { left: 0; top: 380px; }
  .mirrored .contact-email { left: 0; top: 430px; }
  .mirrored .holder-name, .mirrored .phone-number, .mirrored .email-address { opacity: 0.75; }

  .url-blocker {
    position: absolute; left: 22px; top: 346px; width: 320px; height: 113px;
    background: var(--blocker); border-radius: 10px;
    display: flex; align-items: center; padding-left: 18px; gap: 14px;
  }
  .web-address { font-size: 29px; font-weight: 400; color: var(--ink); }
</style>
</head>
<body>
<main class="canvas">

  <!-- Front of card -->
  <section class="card card--front" aria-label="Card front">
    <div class="band band--clear"></div>
    <svg class="chip" viewBox="0 0 82 74" aria-label="Foil chip">
      <defs>
        <linearGradient id="foil-front" x1="0" y1="0" x2="1" y2="1">
          <stop offset="0" stop-color="var(--foil-light)"/>
          <stop offset="1" stop-color="var(--foil-dark)"/>
        </linearGradient>
      </defs>
      <rect x="1" y="1" width="80" height="72" rx="8" fill="url(#foil-front)" stroke="var(--foil-line)" stroke-width="1.5"/>
      <g fill="none" stroke="var(--foil-line)" stroke-width="1.5">
        <path d="M1 24 H26 M1 50 H26 M56 24 H81 M56 50 H81"/>
        <rect x="26" y="14" width="30" height="46" rx="4"/>
        <path d="M41 1 V14 M41 60 V73"/>
      </g>
    </svg>
    <div class="front-details">
      <h1 class="holder-name"><span class="given">DANA</span> <span class="family">MERCER</span></h1>
      <p class="contact-line contact-phone">
        <svg width="36" height="36" viewBox="0 0 24 24" aria-hidden="true"><path fill="var(--ink-soft)" d="M6.6 10.8a15.1 15.1 0 0 0 6.6 6.6l2.2-2.2c.3-.3.7-.4 1-.2 1.1.4 2.3.6 3.6.6.6 0 1 .4 1 1V20c0 .6-.4 1-1 1A17 17 0 0 1 3 4c0-.6.4-1 1-1h3.5c.6 0 1 .4 1 1 0 1.3.2 2.5.6 3.6.1.3 0 .7-.2 1z"/></svg>
        <span class="phone-number">555 210 4839</span>
      </p>
      <p class="contact-line contact-email">
        <svg width="38" height="26" viewBox="0 0 38 26" aria-hidden="true"><rect width="38" height="26" fill="var(--ink)"/><path d="M1 1 L19 15 L37 1" fill="none" stroke="#fff" stroke-width="2.5"/></svg>
        <span class="email-address">dmercer@brimly.com</span>
      </p>
    </div>
    <div class="brand-lockup">
      <span class="brand-dot"></span>
      <span class="brand-name">Vex</span>
    </div>
  </section>

  <!-- Back of card -->
  <section class="card card--back" aria-label="Card back">
    <div class="band band--magstripe"></div>
    <svg class="chip" viewBox="0 0 82 74" aria-label="Foil chip">
      <defs>
        <linearGradient id="foil-back" x1="0" y1="0" x2="1" y2="1">
          <stop offset="0" stop-color="var(--foil-light)"/>
          <stop offset="1" stop-color="var(--foil-dark)"/>
        </linearGradient>
      </defs>
      <rect x="1" y="1" width="80" height="72" rx="8" fill="url(#foil-back)" stroke="var(--foil-line)" stroke-width="1.5"/>
      <g fill="none" stroke="var(--foil-line)" stroke-width="1.5">
        <path d="M1 24 H26 M1 50 H26 M56 24 H81 M56 50 H81"/>
        <rect x="26" y="14" width="30" height="46" rx="4"/>
        <path d="M41 1 V14 M41 60 V73"/>
      </g>
    </svg>
    <div class="mirrored" aria-label="Front details seen through the card">
      <p class="holder-name"><span class="given">DANA</span> <span class="family">MERCER</span></p>
      <p class="contact-line contact-phone">
        <svg width="36" height="36" viewBox="0 0 24 24" aria-hidden="true"><path fill="var(--ink-soft)" d="M6.6 10.8a15.1 15.1 0 0 0 6.6 6.6l2.2-2.2c.3-.3.7-.4 1-.2 1.1.4 2.3.6 3.6.6.6 0 1 .4 1 1V20c0 .6-.4 1-1 1A17 17 0 0 1 3 4c0-.6.4-1 1-1h3.5c.6 0 1 .4 1 1 0 1.3.2 2.5.6 3.6.1.3 0 .7-.2 1z"/></svg>
        <span class="phone-number">555 210 4839</span>
      </p>
      <p class="contact-line contact-email">
        <svg width="38" height="26" viewBox="0 0 38 26" aria-hidden="true"><rect width="38" height="26" fill="var(--ink)"/><path d="M1 1 L19 15 L37 1" fill="none" stroke="#fff" stroke-width="2.5"/></svg>
        <span class="email-address">dmercer@brimly.com</span>
      </p>
    </div>
    <div class="url-blocker">
      <svg width="34" height="34" viewBox="0 0 24 24" aria-hidden="true">
        <g fill="none" stroke="var(--ink)" stroke-width="1.8">
          <circle cx="11" cy="11" r="9"/>
          <ellipse cx="11" cy="11" rx="4" ry="9"/>
          <path d="M2 11 H20 M4 6 H18 M4 16 H18"/>
        </g>
        <path d="M14 14 L22 17 L18.5 18.5 L17 22 Z" fill="var(--ink)" stroke="#fff" stroke-width="1"/>
      </svg>
      <span class="web-address">www.vex-kl.com</span>
    </div>
  </section>

</main>
</body>
</html>
```